Expanding into international markets & need a new web design

This website is for our products called "Frostivo". They are gel-ice packs that are used to keep other products cold or frozen. Commonly used for seafood, meat, vaccines and produce. We have recently started selling these products in the UK & Australia so need to upgrade our website to look more professional & modern.
Please use our main company colors are #1F419B & #2F4F4F.
Main product selling points that could be featured:
- USFDA & EU approved
- Keeps products chilled for longer
- Reuseable & economical
There is no online shop required at the moment, the website is just an online catalogue to promote the products and get international distributor contact information.
Just home page layout design is required at the moment.
Our existing website is www.frostivo-packs.example where you can find more information, our logo & pictures.
Target Market(s)
Fishing & seafood industry mainly.
Number of Pages Required
1 page

```html
<!DOCTYPE html>
<html lang="en">
<head>
<meta charset="utf-8">
<title>Frostivo Gel-Ice Packs</title>
<link href="https://fonts.googleapis.com/css2?family=Lato:wght@400;700&family=Oswald:wght@400&family=Arimo:wght@700&display=swap" rel="stylesheet">
<style>
:root{
  --brand:#1f419b;
  --brand-dark:#17337f;
  --accent:#0a8fd0;
  --slate:#2f4f4f;
  --page:#eeeeee;
  --text:#222;
  --muted:#3a3a3a;
  --footer:#3b7fc6;
  --white:#fff;
}
*{margin:0;padding:0;box-sizing:border-box}
html,body{width:977px;height:1200px;overflow:hidden}
body{position:relative;background:var(--page);font-family:"Lato",sans-serif;color:var(--text)}
.abs{position:absolute}
.header{left:0;top:0;width:977px;height:54px;background:var(--white)}
.follow{left:99px;top:21px;font:700 12px "Arimo",sans-serif;color:var(--slate);white-space:nowrap}
.social{top:19px;width:18px;height:18px;border-radius:50%;background:#ddd}
.social.tw{background:var(--accent)}
.brand{left:418px;top:14px;display:flex;align-items:center;gap:7px;font:700 25px "Lato",sans-serif;color:var(--brand)}
.brand i{width:14px;height:14px;border-radius:50%;background:var(--brand);display:block}
.call{left:747px;top:8px;width:130px;height:37px;background:var(--brand);border-radius:3px;color:var(--white)}
.call svg{position:absolute;left:4px;top:5px}
.call span{position:absolute;left:34px;top:3px;font:700 10px "Lato",sans-serif}
.call strong{position:absolute;left:34px;top:16px;font:700 14px "Lato",sans-serif;white-space:nowrap}
.nav{left:0;top:54px;width:977px;height:36px;background:linear-gradient(#2453b6,var(--brand-dark))}
.nav a{position:absolute;top:0;height:36px;font:700 10.5px "Lato",sans-serif;line-height:36px;color:var(--white);text-decoration:none;text-align:center;white-space:nowrap}
.nav a.on{background:var(--accent)}
.nav .sep{position:absolute;top:0;width:1px;height:36px;background:#143071}
.slider{left:99px;top:101px;width:779px;height:353px;background:var(--white);padding:3px}
.slide{position:relative;width:100%;height:100%;background:radial-gradient(circle at 75% 40%,#8a847c,#57524c 70%);overflow:hidden}
.photo{position:absolute;right:0;top:0;width:400px;height:347px;background:radial-gradient(ellipse at 50% 45%,#8fd3f7,#2c93d8 45%,rgba(60,60,60,0) 72%)}
.slide h1{position:absolute;left:21px;top:60px;font:400 33px "Oswald",sans-serif;color:var(--white);letter-spacing:-.5px}
.slide p{position:absolute;left:21px;top:128px;width:380px;font:700 13px/19px "Lato",sans-serif;color:var(--white)}
.point{position:absolute;left:20px;height:32px}
.point b{position:absolute;left:0;top:-5px;z-index:1;font:400 38px "Oswald",sans-serif;line-height:42px;color:var(--white)}
.point span{position:absolute;left:15px;top:0;width:290px;height:32px;background:var(--accent);color:var(--white);font:400 14px/32px "Oswald",sans-serif;padding-left:15px;white-space:nowrap}
.dots{position:absolute;left:19px;top:383px;display:flex;gap:5px}
.dots i{width:11px;height:11px;border-radius:50%;background:#3a3835;display:block}
.dots i.on{background:var(--white);border:3px solid var(--brand)}
.card{background:var(--white);border:1px solid #e0e0e0}
.why{left:99px;top:489px;width:779px;height:289px}
.why h2{position:absolute;left:21px;top:21px;width:377px;height:30px;border-bottom:1px solid #bbb;font:700 21px "Arimo",sans-serif;line-height:28px;color:#222;padding-left:38px}
.why h2 em{font-style:normal;color:var(--brand)}
.why h2 i{position:absolute;left:0;top:0;width:30px;height:28px;background:var(--brand)}
.checks{position:absolute;left:21px;top:62px;list-style:none}
.checks li{height:25px;font:400 12px "Lato",sans-serif;line-height:16px;padding-left:18px;position:relative;white-space:nowrap}
.checks li svg{position:absolute;left:0;top:4px}
.why .intro{position:absolute;left:19px;top:215px;width:400px;font:400 11.5px/17.5px "Lato",sans-serif;color:var(--muted)}
.boxshot{position:absolute;left:432px;top:21px;width:326px;height:225px;border:1px solid #ccc;padding:3px;background:var(--white)}
.boxshot div{width:100%;height:100%;background:radial-gradient(circle at 50% 55%,#f0e6cf,#d9d9d9 60%,#cfcfcf)}
.features{left:99px;top:806px;width:779px;height:210px}
.feature{position:absolute;top:21px;width:355px;height:167px;border:1px solid #5d79c9;background:#f4f4f4}
.feature h3{position:absolute;left:32px;top:0;width:290px;height:39px;background:var(--brand);border-radius:0 0 20px 20px;color:var(--white);font:700 14px/15px "Arimo",sans-serif;text-align:center;padding-top:5px}
.feature p{position:absolute;left:11px;top:53px;width:338px;font:400 11.5px/17px "Lato",sans-serif;color:var(--muted)}
.btn{position:absolute;left:118px;top:131px;width:117px;height:25px;background:var(--accent);color:var(--white);font:700 11.5px/25px "Lato",sans-serif;text-align:center}
.strip{left:0;top:1048px;width:977px;height:26px;background:var(--brand);color:var(--white);font:400 11px/26px "Lato",sans-serif}
.strip .l{position:absolute;left:99px;font-weight:700}
.strip .r{position:absolute;right:99px}
.footer{left:0;top:1074px;width:977px;height:126px;background:var(--footer);color:var(--white);font:400 10px "Lato",sans-serif}
.flinks{position:absolute;left:101px;top:27px;font-size:10.5px}
.flinks span{margin:0 7px}
.fbrand{position:absolute;left:680px;top:32px;font:700 19px "Lato",sans-serif;display:flex;align-items:center;gap:6px}
.fbrand i{width:11px;height:11px;border-radius:50%;background:var(--white);display:block}
.addr{position:absolute;left:117px;top:60px;line-height:15px}
.contact{position:absolute;left:296px;line-height:14px}
.copy{position:absolute;right:99px;top:92px}
</style>
</head>
<body>
<header class="abs header">
  <div class="abs follow">FOLLOW US</div>
  <span class="abs social" style="left:180px"></span>
  <span class="abs social tw" style="left:207px"></span>
  <span class="abs social" style="left:234px"></span>
  <span class="abs social" style="left:261px"></span>
  <div class="abs brand"><i></i>Frostivo</div>
  <div class="abs call">
    <svg width="26" height="26" viewBox="0 0 26 26"><circle cx="13" cy="13" r="12" fill="none" stroke="#fff" stroke-width="1.5"/><path d="M9 7l3 0 1 4-2 1c1 2 2 3 4 4l1-2 4 1 0 3c-6 0-11-5-11-11z" fill="#fff"/></svg>
    <span>Call Us Today</span><strong>555-014-2290</strong>
  </div>
</header>
<nav class="abs nav">
  <a class="on" style="left:99px;width:67px">HOME</a>
  <a style="left:166px;width:85px">BENEFITS</a><i class="sep" style="left:251px"></i>
  <a style="left:251px;width:155px">PRODUCT SPECIFICATIONS</a>
  <a style="left:562px;width:167px">FROSTIVO APPLICATIONS</a><i class="sep" style="left:729px"></i>
  <a style="left:729px;width:85px">PACKAGING</a><i class="sep" style="left:814px"></i>
  <a style="left:814px;width:75px">CONTACT</a>
</nav>
<section class="abs slider">
  <div class="slide">
    <div class="photo" role="img" aria-label="Photo of a blue segmented gel-ice pack with ice cubes"></div>
    <h1>OUR PRODUCTS BENEFITS</h1>
    <p>Duis Aute Irure Dolor In Reprehenderit In Voluptate Velit Esse Cillum Amet Consuptre Dipsing.</p>
    <div class="point" style="top:193px"><b>1</b><span>SUPERIOR TO FLAKE ICE</span></div>
    <div class="point" style="top:246px"><b>2</b><span>SEGMENTED CELLS ARE UNIQUE TO FROSTIVO.</span></div>
    <div class="point" style="top:299px"><b>3</b><span>CONVENIENT, CLEAN AND EFFICIENT</span></div>
    <div class="dots"><i class="on"></i><i></i><i></i><i></i></div>
  </div>
</section>
<section class="abs card why">
  <h2><i></i>Why Use <em>Frostivo?</em></h2>
  <ul class="checks">
    <li><svg width="12" height="12"><path d="M1 6l4 5 6-10" fill="none" stroke="#1f67c9" stroke-width="1.6"/></svg>Cost and time saving compared to flake ice</li>
    <li><svg width="12" height="12"><path d="M1 6l4 5 6-10" fill="none" stroke="#1f67c9" stroke-width="1.6"/></svg>Frostivo lasts longer &amp; maintains more constant temperature</li>
    <li><svg width="12" height="12"><path d="M1 6l4 5 6-10" fill="none" stroke="#1f67c9" stroke-width="1.6"/></svg>Segmented pads provide excellent chill distribution</li>
    <li><svg width="12" height="12"><path d="M1 6l4 5 6-10" fill="none" stroke="#1f67c9" stroke-width="1.6"/></svg>High grade film is durable and puncture resistant</li>
    <li><svg width="12" height="12"><path d="M1 6l4 5 6-10" fill="none" stroke="#1f67c9" stroke-width="1.6"/></svg>Reuseable and food safe USFDA Approved</li>
    <li><svg width="12" height="12"><path d="M1 6l4 5 6-10" fill="none" stroke="#1f67c9" stroke-width="1.6"/></svg>Packaged ready for quick freezing</li>
  </ul>
  <p class="intro">Frostivo Gel-Ice Packs are an effective and reliable ice replacement for chilling products during transit. They have been developed through extensive research and testing.</p>
  <div class="boxshot"><div role="img" aria-label="Photo of an open shipping carton filled with gel-ice packs"></div></div>
</section>
<section class="abs card features">
  <div class="feature" style="left:22px">
    <h3>Keep Your Products Chilled<br>For Longer</h3>
    <p>Frostivo Gel-Ice Packs are filled with a specially formulated gel that lasts longer than conventional ice packs. This provides assurance that your products are protected against unexpected delays during transit or air freight.</p>
    <span class="btn">LEARN MORE »</span>
  </div>
  <div class="feature" style="left:403px">
    <h3>Versatile, Reuseable And<br>Puncture Resistant</h3>
    <p>Frostivo Gel-Ice Packs are segmented and flexible and packed into cartons with pop-out ends for faster freezing. The Frostivo transit chill system will keep your costs and temperatures down.</p>
    <span class="btn">LEARN MORE »</span>
  </div>
</section>
<div class="abs strip">
  <span class="l">Frostivo Ice Packs Are Effective &amp; Reliable Ice Replacement Products</span>
  <span class="r">More information about <b>Frostivo Gel-Ice Products</b> &nbsp;✉ <b>Contact us</b></span>
</div>
<footer class="abs footer">
  <div class="flinks">Home<span>|</span>Benefits<span>|</span>Product Specifications<span>|</span>Frostivo Applications<span>|</span>Packaging<span>|</span>Contact</div>
  <svg class="abs" style="left:99px;top:59px" width="9" height="12" viewBox="0 0 9 12"><path d="M4.5 0a4.5 4.5 0 0 0-4.5 4.5c0 3 4.5 7.5 4.5 7.5s4.5-4.5 4.5-7.5A4.5 4.5 0 0 0 4.5 0z" fill="#fff"/><circle cx="4.5" cy="4.5" r="1.6" fill="#3b7fc6"/></svg>
  <div class="addr"><b>Frostivo</b><br>Lorem Ipsum, amet conseptre<br>Harbor Bay, MI 40000</div>
  <svg class="abs" style="left:277px;top:62px" width="11" height="11" viewBox="0 0 11 11"><path d="M1 1l3 0 1 3-2 1c1 2 2 3 4 4l1-2 3 1 0 3C5 11 0 6 1 1z" fill="#fff"/></svg>
  <div class="contact" style="top:63px"><b>Phone :</b> 555-014-2290</div>
  <svg class="abs" style="left:277px;top:86px" width="12" height="11" viewBox="0 0 12 11"><rect x="3" y="0" width="6" height="3" fill="#fff"/><rect x="0" y="3" width="12" height="5" fill="#fff"/><rect x="3" y="7" width="6" height="4" fill="#fff"/></svg>
  <div class="contact" style="top:87px"><b>Fax :</b> 555-014-2291</div>
  <div class="fbrand"><i></i>Frostivo</div>
  <div class="copy">Copyright © 2013 Frostivo Products. All rights reserved.</div>
</footer>
</body>
</html>
```